Your Health, Your Time, Your Way: Personalized, Concierge Care Elevated to Modern Medicine

We need to incorporate an image of our new doctor (Dr. Malvina Okoruwe, MD) with our office logo ( Harborline Family Clinic) and dialogue that shows how simple it is to schedule a free consult and learn what our office has to offer patients. The colors should be consistent with our website- the CMYK codes will be attached for your use below. The font should be easy to read. The text should be clear, and convey value to the patient for chosing us over anyone else ( we offer primary care, preventive medicine, urgen care and functional medicine with 24 hour direct access to care with some of our strengths including focus on individualized care, cutting edge medicine, blended functional and traditional style. We aim to transform lives through patient centered innovative and individualized care plan. I have attached a "mock" image but the details ( office address, name, phone number are incorrect) The correct info is Harborline Family Clinic 4187 Wrenfield Ave Suite 214, Clearwater, FL 33759 and phone number (727)482-3095. A possible hook could read: welcoming new patients now- Your Health, Your Time, Your Way: Personalized Care Meets Modern Medicine
Updates

I did not realize that there was a tab with more information to fill for the designers to see, or for me to upload the basic information they need to create the design.

Target Market(s)

Patients over 18 years of age with interest in longevity, functional and traditional medicine; the postcards will be mailed to our CURRENT patients, and they are a reminder of what we do, new patient availability AND a request for them to refer friends or families

Industry/Entity Type

medical

Font styles to use
Sans Serif

Colors

Designer to choose colors to be used in the design.

Requirements
Must have
• simple reminder to current patients of what we offer, and a call to action for our patients to refer friends and family for same level of excellence;consistency with brand ( see business card and cmyx codes for colors);photo of new physician; logo Harborline Family Clinic, web site (https://harborlinefamilyclinic.net); Must clearly express accepting new patients; simple to call/email to schedule free consultation;; include our email (office@harborlinefamilyclinic.org), phone number (727)482-3095; our address 4187 Wrenfield Ave Suite 214, Clearwater, FL 33759
Nice to have
• photo of our new physician ( in blue jacket: Dr. Malvina Okoruwe, MD) should not take up too much space
Should not have
• clutter, or close text; full sentences( bulleted text preferred)

```html
<!DOCTYPE html>
<html lang="en">
<head>
<meta charset="utf-8">
<title>Harborline Family Clinic – New Patient Postcard</title>
<link rel="stylesheet" href="https://fonts.googleapis.com/css2?family=Poppins:wght@400;500;600;700;800&display=swap">
<style>
  :root {
    --teal: #0a8796;
    --teal-dark: #066f7d;
    --teal-light: #5cc3d6;
    --cream: #f2efb4;
    --cream-line: #e6e1a0;
    --ink: #1c1c1c;
    --paper: #ffffff;
    --stage: #d9d9d9;
    --stamp: #b8babd;
    --photo-a: #c9c6cc;
    --photo-b: #9a9aa3;
  }
  * { box-sizing: border-box; margin: 0; padding: 0; }
  html, body { width: 1067px; height: 1200px; overflow: hidden; }
  body {
    background: var(--stage);
    font-family: "Poppins", sans-serif;
    color: var(--ink);
    position: relative;
  }
  .postcard {
    position: absolute;
    left: 127px;
    width: 813px;
    height: 543px;
    background: var(--paper);
    overflow: hidden;
    box-shadow: 0 2px 8px rgba(0,0,0,.12);
  }
  .postcard--front { top: 40px; }
  .postcard--back { top: 617px; }

  /* ---------- Front ---------- */
  .brand-block {
    position: absolute; left: 0; top: 0; width: 318px; height: 265px;
    background: linear-gradient(135deg, #f1f2f3, #ffffff 60%);
    display: flex; align-items: center; justify-content: center; gap: 12px;
    padding: 0 30px;
  }
  .brand-dot {
    width: 22px; height: 22px; border-radius: 50%; background: var(--teal); flex: none;
  }
  .brand-name {
    font-weight: 500; font-size: 30px; line-height: 1.15; color: var(--ink);
  }
  .team-photo {
    position: absolute; left: 318px; top: 0; width: 495px; height: 265px;
    background: linear-gradient(160deg, var(--photo-a), var(--photo-b));
  }
  .accent-square {
    position: absolute; left: 0; top: 268px; width: 35px; height: 88px;
    background: var(--teal-light);
  }
  .headline-band {
    position: absolute; left: 45px; top: 268px; width: 768px; height: 88px;
    background: var(--teal);
    display: flex; align-items: center; justify-content: center;
  }
  .headline {
    color: #fff; font-weight: 700; font-size: 26px; line-height: 1.2;
    text-align: center; text-transform: uppercase;
  }
  .benefits {
    position: absolute; left: 70px; top: 370px; width: 690px;
    list-style: none;
    display: grid; grid-template-columns: 1fr 1fr; column-gap: 30px; row-gap: 4px;
    font-size: 12.5px; line-height: 1.35; font-weight: 500;
  }
  .benefits li { display: flex; align-items: center; gap: 8px; }
  .benefits svg { flex: none; }
  .call-to-action {
    position: absolute; left: 40px; top: 440px; width: 733px;
    text-align: center; font-size: 12.5px; line-height: 1.45;
  }
  .call-to-action .consult { font-weight: 600; }
  .call-to-action .referral { font-weight: 600; color: var(--teal); }
  .front-footer {
    position: absolute; left: 0; bottom: 0; width: 100%; height: 56px;
    background: var(--cream);
    display: flex; align-items: center; justify-content: center;
    font-size: 12.5px; font-weight: 600;
  }
  .front-footer .name { color: var(--teal); margin-right: 4px; }

  /* ---------- Back ---------- */
  .info-panel {
    position: absolute; left: 0; top: 0; width: 407px; height: 345px;
    background: linear-gradient(160deg, var(--teal), var(--teal-dark));
  }
  .info-title {
    position: absolute; left: 40px; top: 24px; width: 340px;
    color: #fff; font-weight: 700; font-size: 15.5px; line-height: 1.25;
  }
  .section-label {
    position: absolute; height: 27px; border-radius: 0 14px 14px 0;
    background: var(--cream); color: var(--teal-dark);
    font-weight: 600; font-size: 16px; line-height: 27px; padding-left: 52px;
  }
  .section-label--traditional { left: 0; top: 76px; width: 255px; }
  .section-label--functional { left: 0; top: 218px; width: 260px; }
  .section-box {
    position: absolute; border: 2px solid var(--cream-line); border-radius: 14px;
    color: #fff; font-size: 10.5px; line-height: 1.25;
  }
  .section-box--traditional {
    left: 35px; top: 90px; width: 320px; height: 118px;
    border-top: none; border-right: none; border-top-left-radius: 0;
    padding: 22px 0 0 16px;
  }
  .section-box--functional {
    left: 35px; top: 232px; width: 338px; height: 156px;
    background: linear-gradient(170deg, var(--teal), var(--teal-dark));
    padding: 26px 14px 0 16px;
    box-shadow: 0 2px 6px rgba(0,0,0,.15);
  }
  .section-box strong { font-weight: 700; }
  .section-box p + p { margin-top: 10px; }
  .treatment-list { list-style: none; margin-top: 6px; font-weight: 500; }
  .treatment-list li { display: flex; align-items: center; gap: 6px; line-height: 1.55; }
  .treatment-list svg { flex: none; }
  .consult-photo {
    position: absolute; left: 283px; top: 104px; width: 142px; height: 142px;
    border-radius: 50%; border: 4px solid #fff;
    background: linear-gradient(140deg, #c89a6a, #e7e7e7 55%, #9aa7ad);
  }
  .doctor-photo {
    position: absolute; left: 40px; top: 394px; width: 120px; height: 120px;
    border-radius: 50%; border: 4px solid #eef0f1;
    background: radial-gradient(circle at 50% 40%, #7b6a66, #2a2a34 70%);
  }
  .contact-list {
    position: absolute; left: 190px; top: 404px; list-style: none;
    font-size: 10.5px; font-weight: 500; line-height: 1.25;
  }
  .contact-list li { display: flex; align-items: flex-start; gap: 8px; margin-bottom: 7px; }
  .contact-list svg { flex: none; margin-top: 1px; }
  .doctor-name {
    position: absolute; left: 170px; top: 494px;
    color: var(--teal); font-weight: 600; font-size: 16px;
  }
  .back-brand {
    position: absolute; left: 450px; top: 40px; width: 170px;
    display: flex; align-items: center; gap: 10px;
  }
  .back-brand .brand-name { font-size: 20px; }
  .back-brand .brand-dot { width: 16px; height: 16px; }
  .stamp-box {
    position: absolute; left: 680px; top: 30px; width: 96px; height: 97px;
    background: var(--stamp);
  }
  .back-footer {
    position: absolute; left: 0; bottom: 0; width: 100%; height: 15px;
    background: var(--cream);
  }
</style>
</head>
<body>

<section class="postcard postcard--front">
  <div class="brand-block">
    <span class="brand-dot"></span>
    <span class="brand-name">Harborline Family Clinic</span>
  </div>
  <div class="team-photo" role="img" aria-label="Photo of three smiling clinic team members, two in white coats, against a soft grey backdrop"></div>
  <div class="accent-square"></div>
  <div class="headline-band">
    <h1 class="headline">Harborline Family Clinic Welcoming<br>New Patients Today!</h1>
  </div>
  <ul class="benefits">
    <li><svg width="10" height="10" viewBox="0 0 8 8"><circle cx="4" cy="4" r="4" fill="#0a8796"/><path d="M2 4.1l1.3 1.3L6 2.7" stroke="#fff" stroke-width="1.1" fill="none"/></svg>Concierge care: your goals, time and health first</li>
    <li><svg width="10" height="10" viewBox="0 0 8 8"><circle cx="4" cy="4" r="4" fill="#0a8796"/><path d="M2 4.1l1.3 1.3L6 2.7" stroke="#fff" stroke-width="1.1" fill="none"/></svg>Easy, direct access to your doctor</li>
    <li><svg width="10" height="10" viewBox="0 0 8 8"><circle cx="4" cy="4" r="4" fill="#0a8796"/><path d="M2 4.1l1.3 1.3L6 2.7" stroke="#fff" stroke-width="1.1" fill="none"/></svg>Individualized care, no insurance algorithms</li>
    <li><svg width="10" height="10" viewBox="0 0 8 8"><circle cx="4" cy="4" r="4" fill="#0a8796"/><path d="M2 4.1l1.3 1.3L6 2.7" stroke="#fff" stroke-width="1.1" fill="none"/></svg>Comfortable one hour or longer visits</li>
    <li><svg width="10" height="10" viewBox="0 0 8 8"><circle cx="4" cy="4" r="4" fill="#0a8796"/><path d="M2 4.1l1.3 1.3L6 2.7" stroke="#fff" stroke-width="1.1" fill="none"/></svg>Cutting edge technology and tests</li>
    <li><svg width="10" height="10" viewBox="0 0 8 8"><circle cx="4" cy="4" r="4" fill="#0a8796"/><path d="M2 4.1l1.3 1.3L6 2.7" stroke="#fff" stroke-width="1.1" fill="none"/></svg>Meet via zoom, by phone or in office</li>
  </ul>
  <div class="call-to-action">
    <p class="consult">Call 727-482-3095 to schedule your free half hour consultation.</p>
    <p class="referral">Love your care? Refer friends and family for the same level of excellence.</p>
  </div>
  <footer class="front-footer">
    <span class="name">Harborline Family Clinic</span> 4187 Wrenfield Ave Suite 214, Clearwater, FL 33759 and phone number (727)482-3095
  </footer>
</section>

<section class="postcard postcard--back">
  <div class="info-panel"></div>
  <h2 class="info-title">Successfully treating chronic illness requires expertise in all areas of medicine.</h2>

  <div class="section-box section-box--traditional">
    <p>Focuses on <strong>symptom-driven</strong> diagnosis<br>and care, offering treatments such as:</p>
    <ul class="treatment-list">
      <li><svg width="8" height="8" viewBox="0 0 8 8"><circle cx="4" cy="4" r="4" fill="#f2efb4"/><path d="M2 4.1l1.3 1.3L6 2.7" stroke="#066f7d" stroke-width="1.1" fill="none"/></svg>Pharmaceutical drugs</li>
      <li><svg width="8" height="8" viewBox="0 0 8 8"><circle cx="4" cy="4" r="4" fill="#f2efb4"/><path d="M2 4.1l1.3 1.3L6 2.7" stroke="#066f7d" stroke-width="1.1" fill="none"/></svg>Procedures</li>
      <li><svg width="8" height="8" viewBox="0 0 8 8"><circle cx="4" cy="4" r="4" fill="#f2efb4"/><path d="M2 4.1l1.3 1.3L6 2.7" stroke="#066f7d" stroke-width="1.1" fill="none"/></svg>Surgery</li>
    </ul>
  </div>
  <div class="section-label section-label--traditional">Traditional Medicine</div>

  <div class="consult-photo" role="img" aria-label="Photo of a patient consultation with a smiling man seated at a table"></div>

  <div class="section-box section-box--functional">
    <p>Focuses on symptoLooks for the <strong>root causes</strong> of symptom as it relates to complex interactions of human body. It seeks to answer “Why are you not well”. It focuses on developing a treatment that <strong>addresses the whole person</strong> rather than a symptom.</p>
    <p>Functional Medicine centers on optimizing crucial elements of health: <strong>diet and nutrition, exercise, sleep, mental health and stress management.</strong></p>
  </div>
  <div class="section-label section-label--functional">Functional Medicine</div>

  <div class="doctor-photo" role="img" aria-label="Portrait photo of Dr. Malvina Okoruwe, MD"></div>

  <ul class="contact-list">
    <li><svg width="11" height="11" viewBox="0 0 12 12"><circle cx="6" cy="6" r="6" fill="#0a8796"/><path d="M4 3.2l1 1.5-.6.7c.4.9 1.1 1.6 2 2l.7-.6 1.5 1-.5 1C5.6 8.6 3.4 6.4 3 4.1z" fill="#fff"/></svg>(727)482-3095</li>
    <li><svg width="11" height="11" viewBox="0 0 12 12"><path d="M6 1a3.6 3.6 0 0 0-3.6 3.6C2.4 7.3 6 11 6 11s3.6-3.7 3.6-6.4A3.6 3.6 0 0 0 6 1z" fill="#0a8796"/><circle cx="6" cy="4.6" r="1.3" fill="#fff"/></svg>harborlinefamilyclinic.net</li>
    <li><svg width="11" height="11" viewBox="0 0 12 12"><circle cx="6" cy="6" r="6" fill="#0a8796"/><rect x="3" y="4" width="6" height="4.2" fill="none" stroke="#fff" stroke-width=".9"/><path d="M3 4l3 2.3L9 4" stroke="#fff" stroke-width=".9" fill="none"/></svg>office@harborlinefamilyclinic.org</li>
    <li><svg width="11" height="11" viewBox="0 0 12 12"><circle cx="6" cy="6" r="6" fill="#0a8796"/><circle cx="6" cy="6" r="2" fill="#fff"/></svg><span>4187 Wrenfield Ave Suite 214,<br>Clearwater, FL 33759</span></li>
  </ul>
  <div class="doctor-name">Dr. Malvina Okoruwe, MD</div>

  <div class="back-brand">
    <span class="brand-dot"></span>
    <span class="brand-name">Harborline Family Clinic</span>
  </div>
  <div class="stamp-box"></div>
  <div class="back-footer"></div>
</section>

</body>
</html>
```